Purchasing community for life science startups needs landing page for collecting of contact adresses

We are the "Pipette Union", the first purchasing community for life science startups. The idea is to bundle the needs of several smaller companies (laboratories) and to buy lab consumables and chemicals in larger quantities. This bargaining position, at the end of all participants can buy their products very low prices. In the attached powerpoint file you will find an idea and some elements, which demonstrate a little the style, which came into my mind.
Urlaub/Ferien
Target Market(s)
Our target customers are startups and smaller biotech companies, which are too small to get the best prices. The aim of this landing page is to collect all interested parties.
Look and feel

```html
<!DOCTYPE html>
<html lang="de">
<head>
<meta charset="utf-8">
<title>Pipette Union – Einkaufsgemeinschaft LifeScience</title>
<link href="https://fonts.googleapis.com/css2?family=Montserrat:wght@400;500;600;700&display=swap" rel="stylesheet">
<style>
:root{
  --blue:#0f97dc;
  --blue-deep:#0a67b3;
  --blue-light:#5fc0ef;
  --navy:#053a6e;
  --ink:#1d1d1f;
  --text:#555a60;
  --muted:#8b9096;
  --page:#f7f8f9;
  --white:#ffffff;
  --field:#f4f5f6;
  --line:#e3e5e8;
}
*{box-sizing:border-box;margin:0;padding:0}
html,body{width:1200px;height:2740px;overflow:hidden}
body{position:relative;background:var(--page);font-family:"Montserrat",Arial,sans-serif;color:var(--ink)}
.abs{position:absolute}

/* hero */
.hero-bg{left:0;top:0;width:1200px;height:600px;
  background:linear-gradient(120deg,#0a70c0 0%,#1692da 45%,#1ea0e2 100%);
  clip-path:polygon(0 0,100% 0,100% 593px,0 490px)}
.hero-art{left:493px;top:128px;width:648px;height:460px;border-radius:8px;
  background:radial-gradient(circle at 50% 45%,rgba(255,255,255,.35),rgba(120,200,240,.15) 60%,rgba(255,255,255,0) 80%)}
.topbar{left:131px;top:29px;width:937px;height:77px;background:var(--white);
  display:flex;align-items:center;justify-content:space-between;padding:0 18px 0 16px;box-shadow:0 2px 8px rgba(0,0,0,.08)}
.brand{display:flex;align-items:center;gap:10px}
.brand-mark{width:48px;height:48px;background:var(--blue-deep)}
.brand-name{font-weight:700;font-size:21px;color:var(--ink);letter-spacing:.2px;line-height:1}
.brand-sub{font-size:11px;color:var(--ink);margin-top:3px}
.contact{display:flex;align-items:center;gap:16px;font-size:14px;font-weight:600}
.contact .or{color:var(--blue);font-weight:600}
.btn{background:var(--blue);color:var(--white);font-weight:700;font-size:13px;letter-spacing:.3px;
  display:flex;align-items:center;justify-content:center;border:none;text-transform:uppercase}
.topbar .btn{width:140px;height:38px}
.hero-title{left:131px;top:296px;color:var(--white);font-weight:700;font-size:34px;line-height:46px}

/* cards */
.card{background:var(--white);border-radius:4px;box-shadow:0 4px 16px rgba(0,0,0,.08);
  display:flex;flex-direction:column;align-items:center;text-align:center;font-size:14.5px;line-height:22px;color:var(--ink)}
.q-card{top:484px;width:283px;height:234px;padding-top:32px}
.q-card p{margin-top:18px;width:220px}
.q-card p.narrow{width:170px}
.hex{width:86px;height:94px}

.campaign{left:131px;top:760px;width:937px;height:104px;background:var(--white);border-radius:4px;
  box-shadow:0 4px 16px rgba(0,0,0,.08);text-align:center;font-size:22px;line-height:32px;font-weight:500;padding-top:19px}
.campaign strong{color:var(--blue);font-weight:700}

/* benefits */
.benefits-bg{left:0;top:900px;width:1200px;height:518px;
  background:linear-gradient(100deg,#4f8fc4 0%,#2b7fc6 40%,#1a74c4 70%,#3b8ece 100%);
  clip-path:polygon(0 0,100% 78px,100% 100%,0 440px)}
.benefits-title{left:0;top:995px;width:1200px;text-align:center;color:var(--white);font-weight:700;font-size:34px}
.b-card{top:1068px;width:283px;height:218px;padding-top:36px}
.b-card p{margin-top:22px;width:266px;font-size:14px}

/* interest */
.interest-title{left:0;top:1452px;width:1200px;text-align:center;font-weight:700;font-size:36px}
.interest-sub{left:0;top:1510px;width:1200px;text-align:center;color:var(--blue);font-size:17px}
.interest-text{left:270px;top:1555px;width:660px;text-align:center;color:var(--text);font-size:14px;line-height:21px}
.form{left:378px;top:1656px;width:444px;height:340px;background:var(--white);border-radius:4px;box-shadow:0 4px 18px rgba(0,0,0,.08)}
.field{position:absolute;left:73px;width:298px;height:38px;background:var(--field);border:1px solid var(--line);
  font-size:12.5px;color:var(--muted);padding:11px 13px;font-family:inherit}
.field.active{background:var(--white);border:1.5px solid #8a8f95;color:var(--ink)}
.field.msg{height:73px}
.form .btn{position:absolute;left:153px;top:272px;width:139px;height:38px}

/* about */
.about-bg{left:0;top:2040px;width:1200px;height:600px;background:var(--white);
  clip-path:polygon(0 0,100% 86px,100% 100%,0 100%)}
.microscope{left:164px;top:2118px;width:274px;height:411px;border-radius:12px;
  background:linear-gradient(180deg,#eef1f5 0%,#dfe4ea 60%,#f2f4f7 100%)}
.point{left:478px;width:560px;display:flex;gap:18px}
.point svg{flex:0 0 58px}
.point p{font-size:14.5px;line-height:22px;color:var(--text)}
.point b{color:var(--blue);font-weight:700}

/* footer */
.footer{left:0;top:2550px;width:1200px;height:190px;background:var(--navy);
  clip-path:polygon(0 6px,100% 89px,100% 100%,0 100%)}
.footer-text{left:0;top:2646px;width:1200px;text-align:center;color:#c8d4e2;font-size:14px;line-height:24px}
</style>
</head>
<body>
<svg width="0" height="0" style="position:absolute">
  <defs>
    <linearGradient id="hexGrad" x1="0" y1="0" x2="0" y2="1">
      <stop offset="0" stop-color="#1aa3e6"/>
      <stop offset="1" stop-color="#0a5ea8"/>
    </linearGradient>
  </defs>
</svg>

<div class="abs hero-bg"></div>
<div class="abs hero-art" role="img" aria-label="Illustration: Wissenschaftler mit DNA-Helix, Atommodell, Laborkolben und Lupe"></div>

<header class="abs topbar">
  <div class="brand">
    <div class="brand-mark"></div>
    <div>
      <div class="brand-name">PIPETTE UNION</div>
      <div class="brand-sub">Einkaufsgemeinschaft LifeScience</div>
    </div>
  </div>
  <div class="contact">
    <svg width="22" height="22" viewBox="0 0 24 24" fill="none" stroke="#1d1d1f" stroke-width="1.6"><path d="M5 3h4l2 5-2.5 1.5a11 11 0 0 0 6 6L16 13l5 2v4a2 2 0 0 1-2 2A17 17 0 0 1 3 5a2 2 0 0 1 2-2z"/></svg>
    <span>CALL : +123 456 7890</span>
    <span class="or">OR</span>
    <span class="btn">Enquire us</span>
  </div>
</header>

<h1 class="abs hero-title">Gemeinsam<br>einkaufen zu<br>Großhandelspreisen</h1>

<div class="abs card q-card" style="left:133px">
  <svg class="hex" viewBox="0 0 86 94"><polygon points="43,2 84,25 84,69 43,92 2,69 2,25" fill="url(#hexGrad)"/>
    <g fill="none" stroke="#fff" stroke-width="2.2"><path d="M36 28h14M39 28v14l-9 18h26l-9-18V28"/><path d="M33 56h20"/></g></svg>
  <p class="narrow">Betreibst du ein LifeScience Labor?</p>
</div>
<div class="abs card q-card" style="left:458px">
  <svg class="hex" viewBox="0 0 86 94"><polygon points="43,2 84,25 84,69 43,92 2,69 2,25" fill="url(#hexGrad)"/>
    <g fill="none" stroke="#fff" stroke-width="2.2"><path d="M31 28h10v30a5 5 0 0 1-10 0zM45 28h10v30a5 5 0 0 1-10 0z"/><path d="M31 44h10M45 40h10"/></g></svg>
  <p>Benötigst du regelmäßig Chemikalien, Laborglas und Verbrauchsmaterialien?</p>
</div>
<div class="abs card q-card" style="left:785px">
  <svg class="hex" viewBox="0 0 86 94"><polygon points="43,2 84,25 84,69 43,92 2,69 2,25" fill="url(#hexGrad)"/>
    <g fill="none" stroke="#fff" stroke-width="2.2"><path d="M46 26h14v14L40 60 26 46z"/><circle cx="54" cy="32" r="2.5"/><path d="M38 48l8-8"/></g></svg>
  <p>Sind deine Abnahmemengen zu klein, um maximale Rabatte zu erhalten?</p>
</div>

<div class="abs campaign">hen take part in the first lab campaign 2019 and<br>Save up to <strong>40%</strong> on purchases.</div>

<div class="abs benefits-bg" role="img" aria-label="Foto: Laborarbeitsplatz mit Glaskolben und Mikroskop, blau eingefärbt"></div>
<h2 class="abs benefits-title">Vorteile</h2>

<div class="abs card b-card" style="left:133px">
  <svg class="hex" viewBox="0 0 86 94"><polygon points="43,2 84,25 84,69 43,92 2,69 2,25" fill="url(#hexGrad)"/>
    <g fill="none" stroke="#fff" stroke-width="2.2"><path d="M24 32h6l5 22h22l4-16H33"/><circle cx="38" cy="60" r="2.5"/><circle cx="54" cy="60" r="2.5"/><path d="M45 40v10M40 45h10"/></g></svg>
  <p>Kaufe ein zu Großhandelspreisen</p>
</div>
<div class="abs card b-card" style="left:458px">
  <svg class="hex" viewBox="0 0 86 94"><polygon points="43,2 84,25 84,69 43,92 2,69 2,25" fill="url(#hexGrad)"/>
    <g fill="none" stroke="#fff" stroke-width="2.2"><path d="M22 42l8-8 8 4 6-4 6 0 14 8"/><path d="M26 46l12 12a3 3 0 0 0 4-4M40 54l4 4a3 3 0 0 0 4-4l-8-8M48 54a3 3 0 0 0 4-4l-8-8"/><path d="M64 42l-6 8"/></g></svg>
  <p>Keine Verhandlungen mit Lieferanten</p>
</div>
<div class="abs card b-card" style="left:785px">
  <svg class="hex" viewBox="0 0 86 94"><polygon points="43,2 84,25 84,69 43,92 2,69 2,25" fill="url(#hexGrad)"/>
    <g fill="none" stroke="#fff" stroke-width="2.2"><path d="M30 26h20l8 8v34H30z"/><path d="M35 38h16M35 45h16M35 52h10"/><path d="M30 26l28 42"/></g></svg>
  <p>Keine Vertragsverpflichtung</p>
</div>

<h2 class="abs interest-title">Hast du Interesse an einer Teilnahme?</h2>
<p class="abs interest-sub">Dann trage dich gerne völlig unverbindlich in unsere Interessentenliste ein.</p>
<p class="abs interest-text">Um einen Eindruck von unseren Preisen zu erhalten schicken wir dir eine vorläufige Preisliste zu und bitten dich um feedback. Welche Artikel interessieren dich? In welchen Mengen benötigst du diese? Welche fehlen noch?</p>

<form class="abs form">
  <div class="field active" style="top:40px">First Name</div>
  <div class="field" style="top:88px">Last Name</div>
  <div class="field" style="top:136px">Email Address</div>
  <div class="field msg" style="top:184px">Message</div>
  <span class="btn">Enquire us</span>
</form>

<div class="abs about-bg"></div>
<div class="abs microscope" role="img" aria-label="Foto: weißes Labormikroskop"></div>

<div class="abs point" style="top:2180px">
  <svg width="58" height="58" viewBox="0 0 58 58" fill="none" stroke="#0f97dc" stroke-width="2"><path d="M8 52h44"/><path d="M12 50V40h6v10M22 50V34h6v16M32 50V28h6v22M42 50V20h6v30"/><path d="M10 30l14-10 10 6 16-16M44 10h6v6"/><path d="M8 8h10M8 13h8M8 18h6"/></svg>
  <p><b>Unser Ziel</b> ist der Aufbau der ersten Einkaufsgemeinschaft für LifeScience Labore, über die jeder Teilnehmer seinen Laborbedarf zu Großhandelspreisen decken kann.</p>
</div>
<div class="abs point" style="top:2268px">
  <svg width="58" height="58" viewBox="0 0 58 58" fill="none" stroke="#0f97dc" stroke-width="2"><path d="M6 22h10l18-12v36L16 34H6z"/><path d="M12 34l4 14h6l-3-14"/><path d="M42 20l8-5M44 28h9M42 36l8 5"/></svg>
  <p><b>Das Kampagnenprinzip.</b> Wir bündeln euren Jahresbedarf an Chemikalien, Verbrauchsmaterialien und Laborbedarf und treten den Herstellern und Lieferanten gegenüber als ein starker Verhandlungspartner auf. Je mehr Teilnehmer mitmachen, desto größer wird unsere Verhandlungsmasse, desto besser unsere Einkaufspreise.</p>
</div>
<div class="abs point" style="top:2424px">
  <svg width="58" height="58" viewBox="0 0 58 58" fill="none" stroke="#0f97dc" stroke-width="2"><path d="M22 30V8a3 3 0 0 1 6 0v18l14 3a4 4 0 0 1 3 5l-3 14a4 4 0 0 1-4 3H26l-12-14a3 3 0 0 1 4-4z"/></svg>
  <p><b>Keep it simple.</b> Wir verzichten auf Rahmenverträge, Mindestbestellmengen und sonstigen Verpflichtungen! Gefällt euch der ausgehandelte Preis, dann bezieht ihr ganz normal per Bestellung bei der Pipette Union euren Bedarf.</p>
</div>

<footer class="abs footer"></footer>
<div class="abs footer-text">Pipette Union Einkaufsgemeinschaft e.K.<br>IMPRESSUM | DATENSCHUTZERKLÄRUNG</div>
</body>
</html>
```